Women & Wealth Program Needs Invitation Design

We are looking for an invitation and save the date for a Women & Wealth Program that we host called Blossomry (logo attached)
I have uploaded an example of previous invitations we have had for Blossomry events. We’d like for the invitation to be feminine but not too cutesy.

We like the size of 8 ½ x 3 ¾ but would be open to a traditional 5x7—2 sided. We will be mailing out a paper invitation and sending out an electronic save the date and invitation.

The program title is “75 is the new 62—how to blossomry(use logo) and plan for longevity.”
Our idea for the front is to have a birthday cake possibly with “75 is the new 62” on the cake with the tagline underneath it.

On the back we would like the following information included:
Join Delia Marsh in this interactive program as she discusses how to eat your cake and have your retirement too. Learn why 75 is the new 62 and how planning for longevity, investing in your own human capital, and finding your next act will help you blossomry in this new age of retirement.

The program will be on Wednesday, February 3 from 6-8pm at MillWarden, 4617 Pebblecrest Rd., Maple Glen, OH 44187
Wine & hors d’oevres will be served.
RSVP by Tuesday, January 26 to Roxanne Walsh at 330-471-6093 or email rwalsh@pqbwealth-example.com

We must include our business logo, contact information, and disclaimer: Delia T. Marsh, CWS, RFA 918 Harrowgate Drive, Suite 410, Brookhaven, OH 44396 www.pqbwealth-example.com
Securities and advisory services offered through Halvern Partners LLC, member NSTB/IPFC. Halvern is under separate ownership from any other entity. (this disclaimer can be as small as 8pt font)

Reason: We would like to have more choices for this unique women's event! Don't be afraid to be edgy!

Target Market(s)

Professional Women-Doctors, Accountants, Business Owners.
Women close to retirement, retired women.

Industry/Entity Type

Financial Service

Font styles to use
Sans Serif
Decorative
Script

Requirements
Must have
• We must include our business logo, contact information, and disclaimer: Delia T. Marsh, CWS, RFA 918 Harrowgate Drive, Suite 410, Brookhaven, OH 44396 www.pqbwealth-example.com
• Securities and advisory services offered through Halvern Partners LLC, member NSTB/IPFC. Halvern is under separate ownership from any other entity. (this disclaimer can be as small as 8pt font)
• The program will be on Wednesday, February 3 from 6-8pm at MillWarden, 4617 Pebblecrest Rd., Maple Glen, OH 44187
• Wine & hors d’oevres will be served.
• RSVP by Tuesday, January 26 to Roxanne Walsh at 330-471-6093 or email rwalsh@pqbwealth-example.com
Nice to have
• The front possibly have a birthday cake with the program title written on it?

```html
<!DOCTYPE html>
<html lang="en">
<head>
<meta charset="utf-8">
<title>75 is the New 62 – Invitation</title>
<link rel="stylesheet" href="https://fonts.googleapis.com/css2?family=Open+Sans:wght@400;600;700&family=Arimo:wght@400;700&family=Kalam:wght@700&display=swap">
<style>
  :root {
    --backdrop: #c0c0c0;
    --card: #ffffff;
    --rose: #cf667a;
    --rose-text: #c75b73;
    --ink: #1a1a1a;
    --cake-cream: #f4f2f0;
    --cake-edge: #e8553c;
  }
  * { box-sizing: border-box; margin: 0; padding: 0; }
  html, body { width: 1200px; height: 1079px; overflow: hidden; }
  body {
    position: relative;
    background: var(--backdrop);
    font-family: "Open Sans", sans-serif;
    color: var(--ink);
  }
  .card { position: absolute; left: 100px; width: 1010px; background: var(--card); }
  .card-front { top: 62px; height: 445px; }
  .card-back { top: 573px; height: 445px; }

  .cake {
    position: absolute; left: 358px; top: 46px; width: 294px; height: 294px;
    border-radius: 50%;
    background: radial-gradient(circle at 50% 50%, var(--cake-cream) 0 58%, var(--cake-edge) 66% 84%, #f0eceb 90%);
    box-shadow: 0 10px 18px rgba(0,0,0,.15);
  }
  .cake-title {
    position: absolute; left: 0; right: 0; top: 76px;
    text-align: center;
    font-family: "Kalam", cursive;
    font-size: 40px; line-height: 44px;
    color: var(--rose-text);
  }
  .tagline {
    position: absolute; left: 0; right: 0; top: 382px;
    text-align: center; font-size: 18px; letter-spacing: 1.2px;
  }
  .tagline .program-name { color: #e79ac0; font-size: 30px; letter-spacing: 0; margin: 0 8px; }

  .invite-band {
    position: absolute; left: 42px; top: 19px; width: 925px; height: 58px;
    background: var(--rose); color: #fff;
    font-size: 24px; font-weight: 400; letter-spacing: 2.4px; text-align: center; line-height: 58px;
  }
  .intro {
    position: absolute; left: 42px; width: 925px; top: 89px;
    text-align: center; font-size: 13.4px; line-height: 16.5px; letter-spacing: .45px;
  }
  .intro strong { font-weight: 600; }
  .details {
    position: absolute; left: 42px; width: 925px; top: 164px;
    text-align: center; font-family: "Arimo", sans-serif; font-size: 15px; line-height: 16.5px; letter-spacing: .2px;
  }
  .brand-row {
    position: absolute; top: 256px; left: 0; right: 0;
    display: flex; justify-content: center; align-items: center; gap: 56px;
  }
  .brand { color: var(--rose-text); font-size: 28px; font-weight: 400; display: flex; align-items: center; gap: 10px; }
  .brand-dot { width: 13px; height: 13px; border-radius: 50%; background: var(--rose-text); }
  .contact {
    position: absolute; left: 0; right: 0; top: 362px;
    text-align: center; font-size: 13px; letter-spacing: .4px;
  }
  .disclaimer {
    position: absolute; left: 42px; top: 391px; width: 925px; height: 32px;
    background: var(--rose); color: #fff;
    font-size: 11.2px; font-weight: 700; letter-spacing: .3px;
    text-align: center; line-height: 32px;
  }
</style>
</head>
<body>
  <section class="card card-front">
    <div class="cake" role="img" aria-label="Photo of a round white frosted birthday cake with a piped orange-red border">
      <p class="cake-title">75<br>is the<br>new 62</p>
    </div>
    <p class="tagline">HOW TO <span class="program-name">blossomry</span> AND PLAN FOR LONGEVITY.</p>
  </section>

  <section class="card card-back">
    <h1 class="invite-band">YOU ARE INVITED</h1>
    <p class="intro">
      Join Delia Marsh in this interactive program as she discusses <strong>how to eat your cake and have your retirement too.</strong><br>
      Learn why 75 is the new 62 and how planning for longevity, investing in your own human capital, and finding your next act<br>
      will help you blossomry in this new age of retirement.
    </p>
    <p class="details">
      <strong>Wednesday, February 3 from 6-8pm | MillWarden,</strong> 4617 Pebblecrest Rd., Maple Glen, OH 44187<br>
      Wine &amp; hors d’oevres will be served.<br>
      RSVP by Tuesday, January 26 to Roxanne Walsh at 330-471-6093 or email rwalsh@pqbwealth-example.com
    </p>
    <div class="brand-row">
      <span class="brand">Blossomry</span>
      <span class="brand"><span class="brand-dot"></span>PQB Wealth</span>
    </div>
    <p class="contact">Delia T. Marsh, CWS, RFA | 918 Harrowgate Drive, Suite 410, Brookhaven, OH 44396 | www.pqbwealth-example.com</p>
    <p class="disclaimer">Securities and advisory services offered through Halvern Partners LLC, member NSTB/IPFC. Halvern is under separate ownership from any other entity.</p>
  </section>
</body>
</html>
```